Business Card & Logo Design

Originally the brief was for a card only - I now think it's probably better to include a logo design as well. PLease add $200 to the Budget of $210, Apologies for the inconvenience for thaos that have already submitted designs.

Lantern Hollow Productions Pty Ltd is a video/dvd/ production company. Primarily corporate medium to high end. It's a one man operation that's been in business 20 years.

The name " Lantern Hollow" is a primarily a reference to Mathieu Corbelle film that's about film making. Shooting "Lantern Hollow" is also a technique employed by cinematographers to make scenes shot in daylight look like night.

See the design emphasising blue day/night tones but open to other ideas.

Main Text can either be Lantern Hollow Productions or Lantern Hollow.

Many thanks to all designers who submitted ideas for this brief.

Choosing between the designs was very difficult indeed.

I wish everyone the best and may the next job be yours!

Warren

• Text for card:
In Larger Print
Lantern Hollow Productions or Lantern Hollow
Warren Bellamy
In Smaller Print
Lantern Hollow Productions Pty Ltd.
17 Pelham Street
Ashwick Vale, VIC, 3188
P: 9734 2061
m: 0438 725 190
e: warrenbellamy@ostrafel.com

```html
<!DOCTYPE html>
<html lang="en">
<head>
<meta charset="utf-8">
<title>Lantern Hollow Productions – Business Card</title>
<link rel="stylesheet" href="https://fonts.googleapis.com/css2?family=Saira:ital,wght@0,300;0,400;0,500;1,300&display=swap">
<style>
  :root {
    --page: #ffffff;
    --card: #8f8d8b;
    --card-edge: #9a9896;
    --logo: #f2f0ee;
    --name: #c6c4c2;
    --ink: #262626;
    --email: #d4d2d0;
    --shadow: rgba(0, 0, 0, 0.35);
  }
  * { margin: 0; padding: 0; box-sizing: border-box; }
  html, body {
    width: 1200px;
    height: 900px;
    overflow: hidden;
    background: var(--page);
  }
  .canvas {
    position: relative;
    width: 1200px;
    height: 900px;
  }
  .card {
    position: absolute;
    left: 300px;
    width: 625px;
    height: 336px;
    border-radius: 28px;
    background: linear-gradient(160deg, var(--card-edge) 0%, var(--card) 55%, #8a8886 100%);
    box-shadow: 2px 4px 6px var(--shadow);
    overflow: hidden;
  }
  .card--front { top: 122px; }
  .card--back  { top: 477px; }

  .wordmark {
    position: absolute;
    font-family: "Saira", sans-serif;
    font-weight: 500;
    font-size: 34px;
    letter-spacing: -0.3px;
    color: var(--logo);
    white-space: nowrap;
    line-height: 1;
  }
  .card--front .wordmark { left: 42px; top: 154px; }
  .card--back .wordmark  { left: 300px; top: 143px; }

  .holder-name {
    position: absolute;
    left: 332px;
    top: 156px;
    font-family: "Saira", sans-serif;
    font-weight: 400;
    font-size: 30px;
    color: var(--name);
    white-space: nowrap;
    line-height: 1;
  }
  .contact {
    position: absolute;
    left: 334px;
    top: 226px;
    font-family: "Saira", sans-serif;
    font-weight: 300;
    font-size: 14.5px;
    line-height: 16px;
    color: var(--ink);
    list-style: none;
    white-space: nowrap;
  }
  .contact .email {
    color: var(--email);
    font-style: italic;
  }
</style>
</head>
<body>
<main class="canvas">
  <section class="card card--front" aria-label="Card front">
    <p class="wordmark">Lantern Hollow</p>
    <h1 class="holder-name">Warren Bellamy</h1>
    <ul class="contact">
      <li>Lantern Hollow Productions Pty Ltd.</li>
      <li>17 Pelham Street</li>
      <li>Ashwick Vale, VIC, 3188</li>
      <li>Phone: 9734 2061</li>
      <li>Mobile: 0438 725 190</li>
      <li class="email">warrenbellamy@ostrafel.com</li>
    </ul>
  </section>
  <section class="card card--back" aria-label="Card back">
    <p class="wordmark">Lantern Hollow</p>
  </section>
</main>
</body>
</html>
```